CHALLENGE! Plimsora is Looking for an Awesome-er Website Designs

Plimsora wants to spotlight your creative website design!
Right now we have the top world class designers that created the best website designs to function as a template, but now we're looking for something awesome-er.
If you're selected, you and your design will be featured on the Plimsora Creator Showcase Page.
Plimsora is a professional website building platform made by designers for designers. Creating a page on Plimsora is really easy - if you can Brushwick you can definitely Plimsora your site.
Plimsora believes in total freedom of website design therefore, the design itself is up to you. Here are some examples: http://www.plimsora-example.com/showcase.html
Fine Print: The winning design must:
- Be designed on www.plimsora-example.com
-Have the homepage only - any other pages are an advantage.
For any assistance, please contact me via the discussion board
Good luck - and may the best design win!
Moira Tallowfen
The homepage can be anything that you choose. Feel free to get creative with it!
Reason: We're extended because we have committed to the payment for the designer.
To make the submission process more clear, simply post your Plimsora site ID in the comments and this will count as your submission.
Reason: Thanks everyone for the submissions. We are extending the date to make sure all the designers were created using Plimsora, because it looks like some submitted only by PSD files.
In for us to consider you, please make sure your site is designed using www.plimsora-example.com and submit the link to the Plimsora published site.
Thanks a lot everyone for all of your hard work!
Hi designers,
Target Market(s)
Web designers and graphic designers
Industry/Entity Type
Building
Requirements
Must have
- The homepage.

```html
<!DOCTYPE html>
<html lang="en">
<head>
<meta charset="utf-8">
<title>Plimsora – Website Designing &amp; Internet Marketing</title>
<link href="https://fonts.googleapis.com/css2?family=Open+Sans:wght@300;400;600;700&family=Questrial&display=swap" rel="stylesheet">
<style>
:root{
  --ink:#111111;
  --band:#000000;
  --dark:#2a2828;
  --banner:#e6e0b6;
  --frame:#7d7d7d;
  --text:#8f8f8f;
  --heading:#3a3a3a;
  --rule:#cfcfcf;
  --white:#ffffff;
  --footer-light:#e4e4e4;
}
*{box-sizing:border-box;margin:0;padding:0}
html,body{width:1061px;height:1200px;overflow:hidden;background:var(--white)}
body{position:relative;font-family:"Open Sans",Arial,sans-serif;color:var(--text)}
.abs{position:absolute}

.brand{left:28px;top:23px;display:flex;align-items:flex-end;gap:8px}
.brand-mark{width:65px;height:64px;background:var(--ink)}
.brand-name{font-weight:700;font-size:20px;color:var(--ink);line-height:1;margin-bottom:0}
.call{right:28px;top:26px;font-size:17px;font-weight:600;letter-spacing:1px;color:var(--ink)}
.search{left:813px;top:63px;width:220px;height:25px;background:var(--ink);color:var(--white);font-size:13px;padding:3px 8px;letter-spacing:.5px}
.search svg{position:absolute;right:6px;top:3px}

.top-band{left:0;top:121px;width:1061px;height:228px;background:var(--band)}
.main-nav{left:0;top:121px;width:1061px;height:46px;display:flex;align-items:center;justify-content:space-between;padding:0 18px 0 32px;color:var(--white);font-size:18px;letter-spacing:.5px}
.main-nav .sep{color:var(--white)}

.banner{left:28px;top:167px;width:1005px;height:342px;background:var(--banner);border:3px solid var(--frame)}
.banner-title{left:20px;top:62px;width:320px;text-align:center;font-family:"Questrial",Arial,sans-serif;font-size:36px;line-height:44px;color:#2b2b2b}
.collage{left:486px;top:47px;width:468px;height:228px;border:3px solid var(--white);background:linear-gradient(120deg,#c0392b 0%,#e07a3a 30%,#7a8a3a 55%,#d84a4a 75%,#b9c8d6 100%)}
.dots{left:459px;top:309px;display:flex;gap:12px}
.dots span{width:13px;height:13px;border-radius:50%;background:var(--white)}
.dots span.on{background:var(--ink)}

.col{top:540px;font-size:13px;line-height:24px;letter-spacing:.4px}
.col h2{font-weight:400;font-size:20px;color:var(--heading);letter-spacing:1px;margin-bottom:12px;line-height:1}
.col ul{list-style:none}
.col li{position:relative;padding-left:25px;margin-bottom:8px}
.col li::before{content:"";position:absolute;left:2px;top:8px;width:10px;height:10px;border-radius:50%;background:#a9a9a9}
.speciality{left:28px;width:290px}
.success{left:380px;width:300px}
.testimonials{left:747px;width:290px}
.quote-by{margin-top:10px;color:var(--ink);font-weight:600}
.vrule{top:565px;width:1px;height:188px;background:var(--rule)}

.hrule{left:28px;width:1005px;height:1px;background:var(--rule)}
.section-title{left:28px;top:808px;font-size:20px;color:var(--heading);letter-spacing:1px}
.projects{left:0;top:845px;width:1061px;height:190px;background:var(--dark)}
.thumb{top:17px;width:192px;height:158px;border:3px solid #dcdcdc}
.arrow{top:75px}

.footer-nav{left:0;top:1099px;width:1061px;text-align:center;font-size:15px;color:var(--ink);letter-spacing:.6px}
.footer-nav .sep{color:#777;margin:0 4px}
.footer-bar{left:0;top:1147px;width:1061px;height:53px;background:var(--dark)}
.copyright{left:16px;top:17px;font-size:13px;color:var(--white)}
.social{left:855px;top:10px;display:flex;gap:7px}
.social span{width:32px;height:32px;border-radius:3px;background:linear-gradient(#f7f7f7,#cfcfcf);border:1px solid #9a9a9a}
</style>
</head>
<body>

<header>
  <div class="abs brand"><div class="brand-mark"></div><span class="brand-name">Plimsora</span></div>
  <div class="abs call">Call : 07 555 0148</div>
  <div class="abs search">Search...
    <svg width="22" height="18" viewBox="0 0 22 18"><circle cx="8" cy="7" r="5" fill="none" stroke="#bbb" stroke-width="2"/><line x1="12" y1="11" x2="19" y2="16" stroke="#bbb" stroke-width="3"/></svg>
  </div>
</header>

<div class="abs top-band"></div>
<nav class="abs main-nav">
  <span>Home</span><span class="sep">|</span><span>About Us</span><span class="sep">|</span><span>Services ▾</span><span class="sep">|</span><span>Pay Monthly</span><span class="sep">|</span><span>Portfolio &amp; Testimonials</span><span class="sep">|</span><span>Blog</span><span class="sep">|</span><span>Contact Us</span>
</nav>

<section class="abs banner">
  <h1 class="abs banner-title" style="font-weight:400">Refreshing Website Designing &amp; Internet Marketing</h1>
  <div class="abs collage" role="img" aria-label="Collage of colourful photos: flowers, fruit, food, money and landscapes"></div>
  <div class="abs dots"><span class="on"></span><span></span><span></span><span></span></div>
</section>

<section class="abs col speciality">
  <h2>OUR SPECIALITY</h2>
  <ul>
    <li>We design affordable websites with a high level of design for your business.</li>
    <li>We have advanced internet strategies and marketing knowledge to help promote your business.</li>
    <li>We design affordable websites with a high level of design for your business.</li>
  </ul>
</section>
<div class="abs vrule" style="left:344px"></div>
<section class="abs col success">
  <h2>WAY TO SUCCESS</h2>
  <p>Brightloom is a web design agency based in Harrowby, Tallis Bay (Coast of Ember), we're a hard working company who are designers, developers and internet marketing specialists who design websites for businesses in Harrowby, Mount Corrin, Tallis Bay, Fenwick and Nationwide.</p>
</section>
<div class="abs vrule" style="left:707px"></div>
<section class="abs col testimonials">
  <h2>TESTIMONIALS</h2>
  <p>Quisque rutrum. Aenean imperdiet. Etiam ultricies nisi vel augue. Curabitur ullamcorper ultricies nisi. Nam eget dui. Etiam rhoncus. Maecenas tempus, tellus eget condimentum rhoncus, sem quam.</p>
  <p class="quote-by">-Orvel Tamsby, Quinlow</p>
</section>

<div class="abs hrule" style="top:787px"></div>
<h2 class="abs section-title" style="font-weight:400">FEATURED PROJECTS</h2>
<section class="abs projects">
  <svg class="abs arrow" style="left:17px" width="26" height="26" viewBox="0 0 26 26"><circle cx="13" cy="13" r="11" fill="none" stroke="#bbb" stroke-width="2"/><path d="M15 8l-6 5 6 5z" fill="#bbb"/></svg>
  <div class="abs thumb" role="img" aria-label="Medical building website screenshot" style="left:61px;background:linear-gradient(#ffffff 0%,#ffffff 15%,#7fa6c9 25%,#c2a27a 55%,#ffffff 70%,#ffffff 100%)"></div>
  <div class="abs thumb" role="img" aria-label="Landscaping website screenshot" style="left:310px;background:linear-gradient(90deg,#b8a88a 0%,#5e9a3a 20%,#6aa83e 80%,#3d7fc4 100%)"></div>
  <div class="abs thumb" role="img" aria-label="Garden website screenshot with trees" style="left:558px;background:linear-gradient(#ffffff 0%,#4f9a35 12%,#8ec65a 35%,#ffffff 45%,#ffffff 85%,#7cc246 100%)"></div>
  <div class="abs thumb" role="img" aria-label="School website screenshot" style="left:807px;background:linear-gradient(#ffffff 0%,#c81f1f 18%,#9a8a80 45%,#c81f1f 70%,#ffffff 80%,#ffffff 100%)"></div>
  <svg class="abs arrow" style="left:1017px" width="26" height="26" viewBox="0 0 26 26"><circle cx="13" cy="13" r="11" fill="none" stroke="#bbb" stroke-width="2"/><path d="M11 8l6 5-6 5z" fill="#bbb"/></svg>
</section>

<div class="abs hrule" style="top:1073px"></div>
<nav class="abs footer-nav">Home<span class="sep">|</span>About Us<span class="sep">|</span>Services<span class="sep">|</span>Pay Monthly<span class="sep">|</span>Portfolio &amp; Testimonials<span class="sep">|</span>Blog<span class="sep">|</span>Contact Us</nav>

<footer class="abs footer-bar">
  <svg class="abs" style="left:778px;top:0" width="283" height="53" viewBox="0 0 283 53"><polygon points="0,0 283,0 283,53 55,53" fill="#555"/><polygon points="8,0 283,0 283,53 62,53" fill="var(--footer-light)"/></svg>
  <div class="abs copyright">Copyright © 2013 plimsora-example.com</div>
  <div class="abs social"><span></span><span></span><span></span><span></span><span></span></div>
</footer>

</body>
</html>
```